Presentation for partners template design for a healthy bakery

A bakery that makes healthy homemade cupcakes, needs a presentation template for wholesale partners. We need 3-4 template pages with pictures and text blocks, one template that can accomodate a pricing table. Just to give you an idea for the templates our final presentation will include:
1. Cover page with logo
2. Intro page about us
3. Detailed description of products
4. Menu table: cupcakes with wholesale pricing
5. Contact page
Updates

Target Market(s)

Food stores, cafés, fitness clubs, pastry shops, etc.

Industry/Entity Type

Bakery

Font styles to use
Sans Serif

Colors
fee3d4
fce8d3
eaf2ce
cadf82
ffffff
000000
cfeae6
ec1f27
86cfc6

Requirements
Must have
• Presentation needs to look serious and professional. The design needs to give an eco feel: we use recycled materials in our packaging and production. Please make sure the fonts you use support Cyrillic.
Nice to have
• The format of pages is either square or horizontal A4. The company mint colour (see logo attached) needs to be used, but other colours can be used in addition (lime green, peach, black, chocolate brown, red, etc). Craft paper texture (like our packaging, see photos) would be nice to have.

```html
<!DOCTYPE html>
<html lang="en">
<head>
<meta charset="utf-8">
<title>Mint Crumb — Partner Presentation Spread</title>
<link href="https://fonts.googleapis.com/css2?family=Cinzel:wght@400;600&family=Montserrat:wght@400;500&display=swap" rel="stylesheet">
<style>
  :root{
    --mint:#3f9e8f;
    --mint-dark:#2f7f72;
    --mint-light:#cfeae6;
    --paper:#ecebea;
    --craft:#ddd3c5;
    --craft-dark:#c9b8a6;
    --red:#d6284a;
    --ink:#2a2a2a;
    --price:#b18468;
    --white:#ffffff;
    --blush:#f2c9cf;
  }
  *{box-sizing:border-box;margin:0;padding:0}
  html,body{width:1200px;height:695px;overflow:hidden;background:#ffffff}
  .spread{position:relative;width:1200px;height:695px;display:flex}
  .page{position:relative;width:600px;height:695px;overflow:hidden}
  .page-menu{
    background:
      radial-gradient(ellipse 160px 120px at 110px 90px,rgba(190,185,180,.28),transparent 70%),
      radial-gradient(ellipse 120px 110px at 520px 110px,rgba(190,185,180,.26),transparent 70%),
      radial-gradient(ellipse 200px 160px at 320px 260px,rgba(255,255,255,.6),transparent 70%),
      linear-gradient(180deg,#f2f1f0 0%,#e9e8e6 100%);
  }
  .page-cover{background:var(--craft)}
  .page svg.bg{position:absolute;inset:0}

  .leaf-spray{position:absolute;border-radius:50%;background:radial-gradient(ellipse at center,rgba(175,170,165,.3) 0%,rgba(175,170,165,0) 70%)}
  .leaf-spray.left{left:60px;top:10px;width:150px;height:150px}
  .leaf-spray.right{left:470px;top:20px;width:130px;height:160px}

  .menu-heading{position:absolute;top:44px;left:0;width:630px;text-align:center}
  .flourish{display:block;margin:0 auto;width:72px;height:6px;border-radius:3px;background:linear-gradient(90deg,transparent,rgba(150,140,110,.55),transparent)}
  .menu-heading h1{font-family:"Cinzel",serif;font-weight:400;font-size:19px;letter-spacing:1px;color:var(--ink);display:inline-flex;align-items:center;gap:12px;margin:4px 0}
  .menu-heading h1::before,.menu-heading h1::after{content:"";display:block;width:85px;height:1px;background:#b9b4ae}
  .menu-heading p{font-family:"Montserrat",sans-serif;font-size:8px;color:var(--ink);margin-top:10px;letter-spacing:.3px}

  .menu-item{position:absolute;display:flex;align-items:center;gap:8px}
  .photo-wrap{position:relative;width:76px;height:76px;flex:none;display:flex;align-items:center;justify-content:center}
  .petals{position:absolute;inset:0;border-radius:50%;background:radial-gradient(circle,rgba(240,180,190,.0) 55%,rgba(240,180,190,.55) 70%,rgba(240,180,190,0) 100%)}
  .menu-photo{position:relative;width:64px;height:64px;border-radius:50%;border:2px solid var(--blush)}
  .p1{background:radial-gradient(circle at 40% 35%,#fbeff0 0%,#e8c1c4 40%,#9ccfc6 75%,#8a6a55 100%)}
  .p2{background:radial-gradient(circle at 55% 30%,#e8f6f3 0%,#6fc4b6 40%,#5b3d2f 80%,#3c2a22 100%)}
  .p3{background:radial-gradient(circle at 45% 40%,#ffffff 0%,#b9dff0 40%,#8ec5e3 65%,#b88460 100%)}
  .p4{background:radial-gradient(circle at 50% 45%,#fbf2d8 0%,#f1c8a4 40%,#d7a0c7 70%,#a9477a 100%)}
  .p5{background:radial-gradient(circle at 45% 35%,#f6ede2 0%,#c9a18b 40%,#5a3428 75%,#2f1b16 100%)}
  .p6{background:radial-gradient(circle at 55% 45%,#f7eccd 0%,#c9995a 40%,#4a3026 70%,#9fc9b4 100%)}
  .menu-text h2{font-family:"Cinzel",serif;font-weight:400;font-size:17px;color:var(--ink);line-height:1}
  .menu-text p{font-family:"Montserrat",sans-serif;font-size:7.5px;color:var(--ink);margin:4px 0 3px 4px}
  .menu-text .price{font-family:"Cinzel",serif;font-size:13px;color:var(--price);margin-left:4px}

  .brand-badge{position:absolute;border-radius:50%;background:var(--mint);display:flex;align-items:center;justify-content:center;text-align:center;font-family:"Montserrat",sans-serif;font-weight:500;color:var(--white)}
  .brand-badge.small{left:41px;top:496px;width:106px;height:106px;font-size:15px;box-shadow:0 0 0 3px var(--craft),0 0 0 4px var(--mint)}
  .brand-badge.large{left:172px;top:300px;width:262px;height:262px;font-size:40px;border:9px solid var(--white);box-shadow:0 0 30px 6px rgba(255,255,255,.55),0 4px 14px rgba(0,0,0,.15)}

  .contact{position:absolute;top:633px;font-family:"Montserrat",sans-serif;font-size:11.5px;color:var(--ink);line-height:19px}
  .contact li{list-style:none;display:flex;align-items:center;gap:8px}
  .contact svg{width:11px;height:11px;flex:none}
  .contact.left{left:38px}
  .contact.right{left:221px}

  .cover-web{position:absolute;left:146px;top:645px;width:300px;text-align:center;font-family:"Montserrat",sans-serif;font-size:16px;letter-spacing:2.6px;color:var(--mint-dark)}
</style>
</head>
<body>
<main class="spread">

  <section class="page page-menu">
    <div class="leaf-spray left" role="img" aria-label="Faint leaf ornament"></div>
    <div class="leaf-spray right" role="img" aria-label="Faint leaf ornament"></div>

    <svg class="bg" viewBox="0 0 600 695" width="600" height="695" aria-hidden="true">
      <defs>
        <radialGradient id="mottleL" cx=".5" cy=".5" r=".5">
          <stop offset="0" stop-color="#c6b6a6" stop-opacity=".45"/>
          <stop offset="1" stop-color="#c6b6a6" stop-opacity="0"/>
        </radialGradient>
        <clipPath id="craftL"><path d="M0,482 C60,465 95,440 150,446 C220,452 270,548 350,546 C440,544 500,440 600,424 L600,695 L0,695 Z"/></clipPath>
      </defs>
      <path d="M0,470 C60,445 95,420 150,424 C220,430 270,526 350,526 C440,524 500,420 600,402 L600,695 L0,695 Z" fill="var(--mint)"/>
      <path d="M0,482 C60,465 95,440 150,446 C220,452 270,548 350,546 C440,544 500,440 600,424 L600,695 L0,695 Z" fill="var(--craft)"/>
      <g clip-path="url(#craftL)" role="img" aria-label="Craft paper texture">
        <ellipse cx="300" cy="560" rx="140" ry="90" fill="url(#mottleL)"/>
        <ellipse cx="520" cy="520" rx="110" ry="70" fill="url(#mottleL)"/>
        <ellipse cx="160" cy="660" rx="160" ry="60" fill="url(#mottleL)"/>
        <ellipse cx="450" cy="660" rx="120" ry="50" fill="url(#mottleL)"/>
      </g>
    </svg>

    <header class="menu-heading">
      <span class="flourish" role="img" aria-label="Scroll ornament"></span>
      <h1>Menu Table</h1>
      <span class="flourish" role="img" aria-label="Scroll ornament"></span>
      <p>CUPCAKES WITH WHOLESALE PRICING</p>
    </header>

    <article class="menu-item" style="left:56px;top:130px">
      <div class="photo-wrap"><span class="petals"></span><div class="menu-photo p1" role="img" aria-label="Cupcake with pastel sprinkles"></div></div>
      <div class="menu-text"><h2>Title Here</h2><p>Lorem Ipsum is simply dummy text</p><div class="price">$ 00.00</div></div>
    </article>
    <article class="menu-item" style="left:321px;top:130px">
      <div class="photo-wrap"><span class="petals"></span><div class="menu-photo p2" role="img" aria-label="Mint frosted chocolate cupcakes"></div></div>
      <div class="menu-text"><h2>Title Here</h2><p>Lorem Ipsum is simply dummy text</p><div class="price">$ 00.00</div></div>
    </article>
    <article class="menu-item" style="left:56px;top:229px">
      <div class="photo-wrap"><span class="petals"></span><div class="menu-photo p3" role="img" aria-label="Blue and white frosted cupcake"></div></div>
      <div class="menu-text"><h2>Title Here</h2><p>Lorem Ipsum is simply dummy text</p><div class="price">$ 00.00</div></div>
    </article>
    <article class="menu-item" style="left:321px;top:229px">
      <div class="photo-wrap"><span class="petals"></span><div class="menu-photo p4" role="img" aria-label="Pastel swirl cupcake"></div></div>
      <div class="menu-text"><h2>Title Here</h2><p>Lorem Ipsum is simply dummy text</p><div class="price">$ 00.00</div></div>
    </article>
    <article class="menu-item" style="left:56px;top:329px">
      <div class="photo-wrap"><span class="petals"></span><div class="menu-photo p5" role="img" aria-label="Tray of chocolate cupcakes"></div></div>
      <div class="menu-text"><h2>Title Here</h2><p>Lorem Ipsum is simply dummy text</p><div class="price">$ 00.00</div></div>
    </article>
    <article class="menu-item" style="left:321px;top:329px">
      <div class="photo-wrap"><span class="petals"></span><div class="menu-photo p6" role="img" aria-label="Chocolate cupcake with cream topping"></div></div>
      <div class="menu-text"><h2>Title Here</h2><p>Lorem Ipsum is simply dummy text</p><div class="price">$ 00.00</div></div>
    </article>

    <div class="brand-badge small">Mint Crumb</div>

    <ul class="contact left">
      <li><svg viewBox="0 0 12 12"><path d="M6 1a3.5 3.5 0 0 0-3.5 3.5C2.5 7.5 6 11 6 11s3.5-3.5 3.5-6.5A3.5 3.5 0 0 0 6 1z" fill="none" stroke="var(--mint-dark)" stroke-width="1.2"/><circle cx="6" cy="4.5" r="1.2" fill="var(--mint-dark)"/></svg>Address Goes Here</li>
      <li><svg viewBox="0 0 12 12"><path d="M2.5 1.5l2 .3.8 2.2-1.2 1a6 6 0 0 0 2.9 2.9l1-1.2 2.2.8.3 2c-4.5.6-8.6-3.5-8-8z" fill="none" stroke="var(--mint-dark)" stroke-width="1.1"/></svg>+0123 456 789</li>
    </ul>
    <ul class="contact right">
      <li><svg viewBox="0 0 12 12"><rect x="1" y="2.5" width="10" height="7" fill="none" stroke="var(--mint-dark)" stroke-width="1.1"/><path d="M1 2.5l5 4 5-4" fill="none" stroke="var(--mint-dark)" stroke-width="1.1"/></svg>info@tourmailid.com</li>
      <li><svg viewBox="0 0 12 12"><circle cx="6" cy="6" r="5" fill="none" stroke="var(--mint-dark)" stroke-width="1.1"/><path d="M1 6h10M6 1c-2.5 3-2.5 7 0 10M6 1c2.5 3 2.5 7 0 10" fill="none" stroke="var(--mint-dark)" stroke-width="1"/></svg>www.yourwebsite.com</li>
    </ul>
  </section>

  <section class="page page-cover">
    <svg class="bg" viewBox="0 0 600 695" width="600" height="695">
      <defs>
        <linearGradient id="heroBase" x1="0" y1="0" x2="1" y2="1">
          <stop offset="0" stop-color="#e9d3d6"/>
          <stop offset=".45" stop-color="#efe6d4"/>
          <stop offset="1" stop-color="#bfd8d0"/>
        </linearGradient>
        <radialGradient id="cream" cx=".5" cy=".5" r=".5">
          <stop offset="0" stop-color="#fdf6dc"/>
          <stop offset=".7" stop-color="#f3e6b8" stop-opacity=".8"/>
          <stop offset="1" stop-color="#f3e6b8" stop-opacity="0"/>
        </radialGradient>
        <radialGradient id="pink" cx=".5" cy=".5" r=".5">
          <stop offset="0" stop-color="#f9dde2"/>
          <stop offset=".6" stop-color="#eeb3bf" stop-opacity=".85"/>
          <stop offset="1" stop-color="#eeb3bf" stop-opacity="0"/>
        </radialGradient>
        <radialGradient id="cake" cx=".5" cy=".5" r=".5">
          <stop offset="0" stop-color="#9a6a4e" stop-opacity=".8"/>
          <stop offset="1" stop-color="#9a6a4e" stop-opacity="0"/>
        </radialGradient>
        <linearGradient id="trayTone" x1="0" y1="0" x2="1" y2="1">
          <stop offset="0" stop-color="#c8ad98"/>
          <stop offset=".4" stop-color="#e8c3c8"/>
          <stop offset=".7" stop-color="#b76b7a"/>
          <stop offset="1" stop-color="#5a3a32"/>
        </linearGradient>
        <radialGradient id="mottle" cx=".5" cy=".5" r=".5">
          <stop offset="0" stop-color="#bfa996" stop-opacity=".45"/>
          <stop offset="1" stop-color="#bfa996" stop-opacity="0"/>
        </radialGradient>
        <filter id="soft" x="-20%" y="-20%" width="140%" height="140%"><feGaussianBlur stdDeviation="10"/></filter>
        <clipPath id="heroClip"><rect x="0" y="0" width="600" height="420"/></clipPath>
        <clipPath id="craftClip"><path d="M0,394 C80,378 170,392 250,424 C350,464 460,560 600,536 L600,695 L0,695 Z"/></clipPath>
      </defs>

      <g clip-path="url(#heroClip)" role="img" aria-label="Close-up of cupcakes topped with white frosting flowers">
        <rect x="0" y="0" width="600" height="420" fill="url(#heroBase)"/>
        <g filter="url(#soft)">
          <ellipse cx="140" cy="150" rx="130" ry="110" fill="url(#cream)"/>
          <ellipse cx="140" cy="110" rx="75" ry="60" fill="url(#pink)"/>
          <ellipse cx="310" cy="230" rx="125" ry="100" fill="url(#cream)"/>
          <ellipse cx="315" cy="190" rx="60" ry="45" fill="url(#pink)"/>
          <ellipse cx="110" cy="320" rx="120" ry="100" fill="url(#cream)"/>
          <ellipse cx="90" cy="210" rx="90" ry="40" fill="url(#cake)"/>
          <ellipse cx="250" cy="300" rx="70" ry="40" fill="url(#cake)"/>
        </g>
      </g>

      <path d="M318,283 C420,300 520,250 600,236 L600,540 C540,520 470,470 380,440 Z" fill="url(#trayTone)" role="img" aria-label="Tray of berry-topped cupcakes"/>
      <path d="M552,0 C610,30 590,120 520,180 C450,240 380,270 318,283 C420,300 520,250 600,236 L600,0 Z" fill="var(--white)"/>
      <path d="M560,0 C605,35 585,125 525,182 C470,232 420,258 372,274 C450,275 530,242 600,226 L600,0 Z" fill="var(--red)"/>

      <path d="M0,390 C80,374 170,388 250,420 C350,460 460,556 600,532" fill="none" stroke="var(--white)" stroke-width="5" opacity=".8"/>
      <path d="M0,394 C80,378 170,392 250,424 C350,464 460,560 600,536 L600,695 L0,695 Z" fill="var(--craft)"/>
      <path d="M0,394 C80,378 170,392 250,424" fill="none" stroke="var(--mint)" stroke-width="3" opacity=".7"/>
      <path d="M440,540 C500,548 560,544 600,536" fill="none" stroke="var(--mint)" stroke-width="4"/>
      <g clip-path="url(#craftClip)" role="img" aria-label="Craft paper texture with faint watercolour stains">
        <ellipse cx="90" cy="470" rx="120" ry="80" fill="url(#mottle)"/>
        <ellipse cx="60" cy="600" rx="90" ry="70" fill="url(#mottle)"/>
        <ellipse cx="420" cy="620" rx="160" ry="70" fill="url(#mottle)"/>
        <ellipse cx="240" cy="680" rx="140" ry="40" fill="url(#mottle)"/>
      </g>
    </svg>

    <div class="brand-badge large">Mint Crumb</div>
    <div class="cover-web">www.yourwebsite.com</div>
  </section>

</main>
</body>
</html>
```